Need Flyer for Our Real estate Agency

Need to run General Campaign for our agency with Start of New Year as our theme ..Must have an agent's picture on the DL..
Address:
27 / 348Marlow rd, Truganina VIC 3029
Ph:03 9412 7305
email:info@koralinrealestate.com.au
www.koralinrealestate.com.au
Something like as attached picture..
Target Market(s)
Home Buyers
Industry/Entity Type
Real Estate Agent
Requirements
Must have
- Our Logo Colours

```html
<!DOCTYPE html>
<html lang="en">
<head>
<meta charset="UTF-8">
<title>Koralin Real Estate – DL Flyer</title>
<link href="https://fonts.googleapis.com/css2?family=Bebas+Neue&family=Montserrat:wght@400;500;600&display=swap" rel="stylesheet">
<style>
  :root {
    --navy: #14205e;
    --crimson: #74151f;
    --white: #ffffff;
    --ink: #1f1f24;
    --page: #ededee;
    --photo-light: #d4d8db;
    --photo-mid: #7d8c93;
    --photo-dark: #3d4950;
  }
  html, body {
    margin: 0;
    padding: 0;
    width: 1099px;
    height: 1200px;
    overflow: hidden;
    background: var(--page);
  }
  .flyer {
    position: absolute;
    left: 30px;
    top: 355px;
    width: 1040px;
    height: 490px;
    overflow: hidden;
    box-shadow: -18px 18px 0 rgba(0,0,0,0.12);
    font-family: "Montserrat", Arial, sans-serif;
  }
  .agent-photo {
    position: absolute;
    inset: 0;
    background:
      radial-gradient(ellipse 22% 40% at 24% 55%, var(--photo-dark) 0%, rgba(61,73,80,0) 100%),
      linear-gradient(100deg, var(--photo-light) 0%, var(--photo-mid) 35%, var(--photo-dark) 60%, var(--photo-mid) 100%);
  }
  .panels {
    position: absolute;
    inset: 0;
    width: 100%;
    height: 100%;
  }
  .brand {
    position: absolute;
    left: 581px;
    width: 400px;
    top: 100px;
    text-align: center;
    color: var(--white);
    font-weight: 500;
    font-size: 30px;
    letter-spacing: 5px;
    line-height: 1;
    white-space: nowrap;
  }
  .tagline {
    position: absolute;
    left: 468px;
    width: 600px;
    top: 164px;
    text-align: center;
    color: var(--white);
    font-family: "Bebas Neue", Impact, sans-serif;
    font-size: 54px;
    letter-spacing: 0;
    line-height: 1;
    white-space: nowrap;
  }
  .call-label {
    position: absolute;
    left: 531px;
    width: 400px;
    top: 256px;
    text-align: center;
    color: var(--white);
    font-size: 36px;
    font-weight: 400;
    line-height: 1;
    white-space: nowrap;
  }
  .phone {
    position: absolute;
    left: 487px;
    width: 500px;
    top: 298px;
    text-align: center;
    color: var(--white);
    font-size: 62px;
    font-weight: 400;
    line-height: 1;
    white-space: nowrap;
  }
  .address {
    position: absolute;
    right: 44px;
    top: 388px;
    color: var(--ink);
    font-size: 26px;
    line-height: 1;
    letter-spacing: 0.5px;
    white-space: nowrap;
  }
  .contact {
    position: absolute;
    top: 437px;
    display: flex;
    align-items: center;
    gap: 10px;
    color: var(--white);
    font-size: 15px;
    font-weight: 500;
    line-height: 1;
    white-space: nowrap;
  }
  .contact--web { left: 392px; }
  .contact--email { left: 728px; }
  .contact svg { width: 16px; height: 16px; flex: none; }
</style>
</head>
<body>
  <main class="flyer">
    <div class="agent-photo" role="img" aria-label="Photo of a smiling real estate agent in a grey suit, arms crossed, in front of a blurred office building"></div>

    <svg class="panels" viewBox="0 0 1175 553" preserveAspectRatio="none" aria-hidden="true">
      <polygon fill="var(--white)" points="600,0 1175,0 1175,553 384,553 424,425 384,328 488,258"/>
      <polygon fill="var(--crimson)" points="612,0 1175,0 1175,424 430,424 392,328 494,262"/>
      <polygon fill="var(--navy)" points="628,0 1175,0 1175,270 518,270"/>
      <polygon fill="var(--navy)" points="415,487 781,487 761,519 405,519"/>
      <polygon fill="var(--crimson)" points="783,487 1175,487 1175,519 763,519"/>
    </svg>

    <div class="brand">KORALIN</div>
    <div class="tagline">Where Dreams Come Home</div>
    <div class="call-label">Call us at</div>
    <div class="phone">03 9412 7305</div>
    <div class="address">27 / 348Marlow rd, Truganina VIC 3029</div>

    <div class="contact contact--web">
      <svg viewBox="0 0 16 16" aria-hidden="true">
        <circle cx="8" cy="8" r="6.5" fill="none" stroke="var(--white)" stroke-width="1.5"/>
        <ellipse cx="8" cy="8" rx="2.8" ry="6.5" fill="none" stroke="var(--white)" stroke-width="1.2"/>
        <line x1="1.5" y1="8" x2="14.5" y2="8" stroke="var(--white)" stroke-width="1.2"/>
      </svg>
      <span>www.koralinrealestate.com.au</span>
    </div>
    <div class="contact contact--email">
      <svg viewBox="0 0 16 16" aria-hidden="true">
        <rect x="1.5" y="3.5" width="13" height="9" fill="none" stroke="var(--white)" stroke-width="1.4"/>
        <polyline points="1.5,3.5 8,9 14.5,3.5" fill="none" stroke="var(--white)" stroke-width="1.4"/>
      </svg>
      <span>info@koralinrealestate.com.au</span>
    </div>
  </main>
</body>
</html>
```